Landscaping business card

We need a business card that reflects our business. We do lawncare and landscaping with all natural materials and have a great track record in the communities we serve: Newton, Brookline, Wellesley, Brighton, Watertown, and Waltham. We have been in business for 10 years.
Updates

I don't know the curvy fonts. Please keep the fonts fairly conservative.

Industry/Entity Type

Landscaping

Contact Information for Business Card

Verbeck Landscaping
Dale Verbeck
Founder and CEO
847 Tarrow Ave
Newton, MA 02317

Requirements
Must have
• The color green

```html
<!DOCTYPE html>
<html lang="en">
<head>
<meta charset="utf-8">
<title>Verbeck Landscaping – Business Card</title>
<link rel="stylesheet" href="https://fonts.googleapis.com/css2?family=Open+Sans:wght@400;600;700;800&display=swap">
<style>
  :root {
    --page-bg: #2b2b2b;
    --card-dark: #2c2c2c;
    --card-mid: #383838;
    --band-dark: #262626;
    --text-grey: #c9c9c9;
    --text-soft: #a8a8a8;
    --leaf-green: #9ccc1f;
    --deep-green: #1f7a2a;
    --stripe-light: #d8d8d8;
    --grass-dark: #2f5a1c;
    --grass-mid: #4f7f2c;
    --grass-light: #6d963c;
    --headline-gold: #c4bf2e;
  }
  * { box-sizing: border-box; margin: 0; padding: 0; }
  html, body {
    width: 1200px; height: 900px; overflow: hidden;
    background: var(--page-bg);
    font-family: "Open Sans", Arial, sans-serif;
  }
  .sheet {
    width: 1200px; height: 900px;
    display: flex; flex-direction: column; align-items: center; justify-content: center;
    gap: 40px;
  }
  .card {
    position: relative;
    width: 700px; height: 400px;
    overflow: hidden;
    box-shadow: 0 10px 30px rgba(0,0,0,.5);
  }

  /* Front */
  .card-front {
    background: linear-gradient(180deg, var(--card-mid) 0%, var(--card-dark) 100%);
    color: var(--text-grey);
  }
  .holder {
    position: absolute; right: 48px; top: 40px; text-align: right;
  }
  .holder-name {
    font-size: 22px; font-weight: 600; letter-spacing: .5px; color: var(--text-grey);
    text-shadow: 0 0 6px rgba(255,255,255,.35);
  }
  .holder-title { font-size: 12px; color: var(--leaf-green); margin-top: 2px; }

  .brand-band {
    position: absolute; left: 0; right: 0; top: 160px; height: 72px;
    background: linear-gradient(180deg, rgba(0,0,0,0) 0%, var(--band-dark) 100%);
    display: flex; align-items: center; padding-left: 34px; gap: 14px;
  }
  .brand-mark {
    width: 46px; height: 46px; background: var(--leaf-green); border-radius: 6px; flex: none;
  }
  .brand-name {
    font-size: 28px; font-weight: 600; color: var(--leaf-green); letter-spacing: .5px; line-height: 1;
  }
  .brand-tagline {
    font-size: 12.5px; font-weight: 600; color: var(--text-soft); margin-top: 5px; letter-spacing: .3px;
  }

  .contacts {
    position: absolute; left: 34px; right: 40px; top: 262px;
    display: grid; grid-template-columns: 1.1fr 1fr 1.2fr; gap: 12px;
    font-size: 12.5px; color: var(--text-grey);
  }
  .contact-item { display: flex; align-items: flex-start; gap: 8px; line-height: 1.7; }
  .contact-item svg { flex: none; margin-top: 4px; }
  .contact-col { display: flex; flex-direction: column; gap: 2px; }

  .bottom-stripe {
    position: absolute; left: 0; right: 0; bottom: 42px; height: 8px;
    background: linear-gradient(180deg, #f2f2f2, var(--stripe-light));
  }
  .bottom-band {
    position: absolute; left: 0; right: 0; bottom: 0; height: 42px;
    background: linear-gradient(180deg, #2a8e36, var(--deep-green));
  }

  /* Back */
  .card-back { background: var(--grass-dark); }
  .grass-field {
    position: absolute; inset: 0;
    background:
      radial-gradient(ellipse at 30% 30%, var(--grass-light) 0%, transparent 60%),
      radial-gradient(ellipse at 75% 70%, var(--grass-mid) 0%, transparent 65%),
      linear-gradient(160deg, var(--grass-mid) 0%, var(--grass-dark) 100%);
  }
  .back-title {
    position: absolute; inset: 0;
    display: flex; flex-direction: column; align-items: center; justify-content: center;
    font-weight: 800; color: var(--headline-gold); line-height: 1.05; text-align: center;
  }
  .back-title .line-one { font-size: 84px; }
  .back-title .line-two { font-size: 96px; }
</style>
</head>
<body>
<main class="sheet">

  <section class="card card-front" aria-label="Business card front">
    <div class="holder">
      <div class="holder-name">DALE VERBECK</div>
      <div class="holder-title">Founder and CEO</div>
    </div>

    <div class="brand-band">
      <span class="brand-mark" aria-hidden="true"></span>
      <div>
        <div class="brand-name">VERBECK LANDSCAPING</div>
        <div class="brand-tagline">We do lawncare and landscaping with all natural materials</div>
      </div>
    </div>

    <div class="contacts">
      <div class="contact-item">
        <svg width="12" height="16" viewBox="0 0 12 16" aria-hidden="true">
          <path d="M6 0C2.7 0 0 2.6 0 5.9 0 10 6 16 6 16s6-6 6-10.1C12 2.6 9.3 0 6 0zm0 8.2A2.3 2.3 0 1 1 6 3.6a2.3 2.3 0 0 1 0 4.6z" fill="var(--leaf-green)"/>
        </svg>
        <span>847 Tarrow Ave Newton,<br>MA 02317</span>
      </div>
      <div class="contact-col">
        <div class="contact-item">
          <svg width="10" height="14" viewBox="0 0 10 14" aria-hidden="true">
            <path d="M2 0h3v4H3.5c0 2 .5 4 1.5 6H6.5v4H3C1 11 0 7 0 4 0 2 1 0 2 0z" fill="var(--leaf-green)"/>
          </svg>
          <span>+(000) 1234 5678</span>
        </div>
        <div class="contact-item">
          <svg width="14" height="13" viewBox="0 0 14 13" aria-hidden="true">
            <rect x="3" y="0" width="8" height="4" fill="var(--leaf-green)"/>
            <rect x="0" y="5" width="14" height="6" rx="1" fill="var(--leaf-green)"/>
            <rect x="3" y="9" width="8" height="4" fill="var(--leaf-green)"/>
          </svg>
          <span>+(000) 1234 5679</span>
        </div>
      </div>
      <div class="contact-col">
        <div class="contact-item">
          <svg width="14" height="14" viewBox="0 0 14 14" aria-hidden="true">
            <circle cx="7" cy="7" r="6.5" fill="var(--leaf-green)"/>
            <path d="M1 7h12M7 .5c2 2 2 11 0 13M7 .5c-2 2-2 11 0 13" stroke="var(--card-dark)" stroke-width="1" fill="none"/>
          </svg>
          <span>www.verbeckland.com</span>
        </div>
        <div class="contact-item">
          <svg width="14" height="10" viewBox="0 0 14 10" aria-hidden="true">
            <rect x=".5" y=".5" width="13" height="9" fill="none" stroke="var(--leaf-green)"/>
            <path d="M.5 .5 7 6l6.5-5.5" fill="none" stroke="var(--leaf-green)"/>
          </svg>
          <span>dale@verbeckland.com</span>
        </div>
      </div>
    </div>

    <div class="bottom-stripe"></div>
    <div class="bottom-band"></div>
  </section>

  <section class="card card-back" aria-label="Business card back">
    <div class="grass-field" role="img" aria-label="Close-up photograph of green lawn grass"></div>
    <div class="back-title">
      <span class="line-one">Verbeck</span>
      <span class="line-two">Landscaping</span>
    </div>
  </section>

</main>
</body>
</html>
```